Website re-design

We are a successful furnished apartment provider in Boston. We currently are working on re-designing our website www.ribtenlofts.com to make it more modern, designer look and user friendly. We hired a designer, but are not happy with the designs proposed and want to improve on them. The winning design will be paid regardless of whether we stay with our current designer or not. We want ideas and functional page links to see how it will work. Platform we have chosen is wordpress. Feel free to propose others easy for us to update and modify. We do not like Joomla on which website is currently running. We do not like flash nor long load times.
Please use photos on our website for design presentations. www.ribtenlofts.com

Target Market(s)

doctors, nurses, business men but mostly business women, some post-medical students

Industry/Entity Type

Apartment

Requirements
Must have
• Quick action button for reservation form and a notification and email forwarding system to us of reservation information by potential clients. Blog required with feedback by guests allowed, we can censor which are published. Slide shows of apartments.
Should not have
• No movies.

```html
<!DOCTYPE html>
<html lang="en">
<head>
<meta charset="utf-8">
<title>Ribten Lofts – The Corporate Stay Apartment 5T</title>
<link href="https://fonts.googleapis.com/css2?family=Arimo:wght@400;700&display=swap" rel="stylesheet">
<style>
:root{
  --black:#000;
  --page-bg:#333333;
  --gold:#d6c38a;
  --gold-dark:#7a6320;
  --card:#ffffff;
  --ink:#2b2b2b;
  --muted:#666;
  --rule:#8a8a8a;
  --panel-top:#e8dcb8;
  --panel-bottom:#d4c08a;
  --offer-bg:#f3f3f3;
  --blue-top:#4a86e0;
  --blue-bottom:#2a5fc4;
}
*{box-sizing:border-box;margin:0;padding:0}
html,body{width:1164px;height:1200px;overflow:hidden}
body{background:var(--page-bg);font-family:"Arimo",Arial,sans-serif;color:var(--ink);position:relative}
a{color:inherit;text-decoration:none}
.abs{position:absolute}

/* header */
.site-header{position:absolute;left:0;top:0;width:1164px;height:143px;background:var(--black)}
.brand{left:154px;top:30px;display:flex;align-items:center;gap:12px}
.brand-mark{width:54px;height:54px;border-radius:50%;background:var(--gold)}
.brand-name{color:var(--gold);font-size:25px;letter-spacing:2px;line-height:1}
.brand-sub{color:var(--gold);font-size:9px;letter-spacing:2.4px;margin-top:6px}
.util-links{right:156px;top:10px;display:flex;align-items:center;gap:14px;color:var(--gold);font-size:11px;letter-spacing:.6px}
.util-links .phone-box{width:22px;height:22px;border-radius:3px;background:#a59a7e;display:flex;align-items:center;justify-content:center}
.util-rule{left:664px;top:41px;width:344px;height:1px;background:#555}
.share-row{right:156px;top:51px;display:flex;align-items:center;gap:16px;color:var(--gold);font-size:11px;letter-spacing:.6px}
.listing-badge{width:70px;height:12px;border-radius:6px;background:#6f6a5b}
.share-icon{width:14px;height:14px;background:var(--gold)}
.main-nav{left:156px;top:114px;display:flex;gap:0;font-size:13px;font-weight:700;letter-spacing:1px;color:var(--gold)}
.main-nav a{margin-right:48px}
.main-nav a.current{color:#fff;position:relative}
.main-nav a.current::after{content:"";position:absolute;left:45px;top:28px;border:6px solid transparent;border-top-color:#000;border-bottom:0}

/* card */
.card{left:154px;top:171px;width:854px;height:957px;background:var(--card)}
.card-bar{left:154px;top:171px;width:854px;height:40px;background:linear-gradient(#fbfbfb,#e6e6e6)}
.back-link{left:168px;top:184px;font-size:13px;color:var(--gold-dark)}
.back-link::before{content:"";display:inline-block;border:4px solid transparent;border-right:5px solid var(--gold-dark);border-left:0;margin-right:6px;vertical-align:1px}
.social{top:183px;height:18px;border:1px solid #c9c9c9;border-radius:2px;background:#f7f7f7;font-size:10px;color:#3b5b99;padding:2px 5px;line-height:12px}

.title{left:180px;top:234px;font-size:29px;font-weight:700;color:#2b2b2b}
.subtitle{left:180px;top:266px;font-size:13px;font-weight:700;color:#777;letter-spacing:.5px}

.tabs{left:180px;top:311px;width:538px;height:28px;border-bottom:1px solid var(--rule)}
.tab{position:absolute;top:0;height:28px;font-size:13px;color:var(--gold-dark);line-height:30px;text-align:center}
.tab + .tab{border-left:1px solid var(--rule)}
.tab.active{color:#222;border:1px solid var(--rule);border-bottom:1px solid #fff;background:#fff;height:29px}

.photo{left:180px;top:348px;width:538px;height:305px;background:linear-gradient(115deg,#6b4520 0%,#d98a3a 35%,#f0b15a 60%,#c96a2c 100%)}
.thumb-marker{left:213px;top:661px;border:6px solid transparent;border-bottom:7px solid #333;border-top:0}
.thumb{top:668px;width:78px;height:52px}
.thumb.active{outline:2px solid #333;outline-offset:-2px}

.section-head{left:180px;font-size:17px;font-weight:700;color:#333}
.section-rule{left:180px;width:538px;height:1px;background:var(--rule)}
.desc{left:181px;top:794px;width:520px;font-size:13px;line-height:16px;color:#222}
.desc strong{display:block}

.offer{left:180px;top:948px;width:538px;height:147px;background:var(--offer-bg)}
.offer-photo{left:200px;top:966px;width:198px;height:110px;background:linear-gradient(120deg,#7a3a18,#e08a3a 50%,#b8321e)}
.offer-title{left:416px;top:961px;font-size:17px;font-weight:700;line-height:22px;color:#333;width:200px}
.offer-price{left:416px;top:1011px;font-size:13px;color:#333}
.offer-link{left:416px;top:1042px;font-size:13px;font-weight:700;color:var(--gold-dark);text-decoration:underline}

/* booking panel */
.booking{left:735px;top:239px;width:245px;height:414px;background:linear-gradient(var(--panel-top),var(--panel-bottom));border-radius:2px}
.price{left:750px;top:252px;font-size:29px;font-weight:700;color:#2b2b2b}
.price small{font-size:17px;font-weight:700}
.booking-rule{left:751px;width:215px;height:1px;background:#b9a774}
.field-label{left:750px;font-size:13px;font-weight:700;color:#2b2b2b}
.field{left:821px;width:145px;height:31px;background:#fff;border:2px solid #c7b78a;border-radius:4px;font-size:13px;color:#888;padding:7px 8px}
.request-btn{left:779px;top:432px;width:158px;height:55px;border-radius:3px;background:linear-gradient(var(--blue-top),var(--blue-bottom));border:1px solid #2852a8;color:#fff;font-size:19px;font-weight:700;text-align:center;line-height:53px;letter-spacing:-.3px}
.hotline{left:740px;top:508px;width:235px;text-align:center;color:#333}
.hotline .h1{font-size:17px;font-weight:700;display:flex;justify-content:center;align-items:center;gap:6px}
.hotline .h2{font-size:17px;font-weight:700;margin-top:1px}
.hotline .h3{font-size:12px;margin-top:4px;line-height:15px}
.hotline .h3 a{text-decoration:underline;color:#222}

.footer{left:153px;top:1140px;font-size:10px;color:#fff;letter-spacing:.3px}
</style>
</head>
<body>

<header class="site-header">
  <div class="abs brand">
    <div class="brand-mark"></div>
    <div>
      <div class="brand-name">RIBTEN LOFTS</div>
      <div class="brand-sub">FURNISHED APARTMENTS</div>
    </div>
  </div>
  <div class="abs util-links">
    <span class="phone-box"><svg width="12" height="12" viewBox="0 0 24 24"><path fill="#fff" d="M6.6 10.8a15.1 15.1 0 0 0 6.6 6.6l2.2-2.2c.3-.3.7-.4 1-.2 1.1.4 2.3.6 3.6.6.6 0 1 .4 1 1V20c0 .6-.4 1-1 1A17 17 0 0 1 3 4c0-.6.4-1 1-1h3.5c.6 0 1 .4 1 1 0 1.3.2 2.5.6 3.6.1.3 0 .7-.2 1z"/></svg></span>
    <a href="#">CONTACT RIBTEN LOFTS</a><span>|</span><a href="#">ABOUT US</a><span>|</span><a href="#">LINKS</a>
  </div>
  <div class="abs util-rule"></div>
  <div class="abs share-row">
    <span class="listing-badge"></span>
    <span style="display:flex;align-items:center;gap:9px"><span class="share-icon"></span><a href="#">SHARE THIS</a></span>
  </div>
  <nav class="abs main-nav">
    <a href="#" class="current">APARTMENTS</a>
    <a href="#">RATES</a>
    <a href="#">RESERVATIONS</a>
    <a href="#">LOCATION</a>
    <a href="#">BLOG</a>
  </nav>
</header>

<div class="abs card"></div>
<div class="abs card-bar"></div>
<a href="#" class="abs back-link">Back to List</a>
<span class="abs social" style="left:727px">Like</span>
<span class="abs social" style="left:775px;color:#333;background:#fff">18</span>
<span class="abs social" style="left:800px">Send</span>
<span class="abs social" style="left:870px;font-weight:700">+1</span>
<span class="abs social" style="left:907px">Post</span>
<span class="abs social" style="left:964px;width:26px;padding:2px 5px">
  <svg width="16" height="11" viewBox="0 0 16 11"><rect x=".5" y=".5" width="15" height="10" fill="#fff" stroke="#333"/><path d="M.5.5 8 6l7.5-5.5" fill="none" stroke="#333"/></svg>
</span>

<h1 class="abs title">The Corporate Stay Apartment 5T</h1>
<div class="abs subtitle">RIBTEN GUEST LOFTS</div>

<div class="abs tabs">
  <span class="tab active" style="left:14px;width:88px">Photos</span>
  <span class="tab" style="left:102px;width:106px">Availability</span>
  <span class="tab" style="left:208px;width:76px">Rates</span>
  <span class="tab" style="left:284px;width:100px">Amenities</span>
</div>

<div class="abs photo" role="img" aria-label="Photo of the apartment bedroom with orange walls, bed and kitchenette"></div>
<div class="abs thumb-marker"></div>
<div class="abs thumb active" style="left:180px;background:linear-gradient(120deg,#6b4520,#e09a4a)" role="img" aria-label="Bedroom thumbnail"></div>
<div class="abs thumb" style="left:265px;background:linear-gradient(120deg,#3a3010,#e8c030)" role="img" aria-label="Kitchenette thumbnail"></div>
<div class="abs thumb" style="left:349px;background:linear-gradient(120deg,#b8401e,#e0a060)" role="img" aria-label="Bathroom door thumbnail"></div>

<h2 class="abs section-head" style="top:753px">Description</h2>
<div class="abs section-rule" style="top:778px"></div>
<div class="abs desc">
  <strong>Larkin Street Location</strong>
  2nd floor west (sunsets) exposure. Laminate floors, Period detail, fabulous layout, 350 sq ft. wireless DSL, flat screen TV, DVD player, Cotton sheets and towels.
</div>

<h2 class="abs section-head" style="top:918px">Similar Offers</h2>
<div class="abs offer"></div>
<div class="abs offer-photo" role="img" aria-label="Photo of a similar apartment with bed, red sofa and wooden floor"></div>
<div class="abs offer-title">The Corporate Stay Apartment 5T</div>
<div class="abs offer-price">US$ 570 / Week</div>
<a href="#" class="abs offer-link">View apartement</a>

<aside class="abs booking"></aside>
<div class="abs price">US$ 570 <small>/ Week</small></div>
<div class="abs booking-rule" style="top:295px"></div>
<label class="abs field-label" style="top:319px">Check-in</label>
<div class="abs field" style="top:310px">mm/dd/yy</div>
<label class="abs field-label" style="top:361px">Check-out</label>
<div class="abs field" style="top:350px">mm/dd/yy</div>
<div class="abs booking-rule" style="top:397px"></div>
<a href="#" class="abs request-btn">Request now</a>
<div class="abs hotline">
  <div class="h1"><svg width="18" height="18" viewBox="0 0 24 24"><path fill="#333" d="M6.6 10.8a15.1 15.1 0 0 0 6.6 6.6l2.2-2.2c.3-.3.7-.4 1-.2 1.1.4 2.3.6 3.6.6.6 0 1 .4 1 1V20c0 .6-.4 1-1 1A17 17 0 0 1 3 4c0-.6.4-1 1-1h3.5c.6 0 1 .4 1 1 0 1.3.2 2.5.6 3.6.1.3 0 .7-.2 1z"/></svg>Booking Hotline</div>
  <div class="h2">617 555 0142</div>
  <div class="h3">Mo-Sa 9 am - 5 pm (EST)<br>or write us <a href="#">info@ribtenlofts.com</a></div>
</div>

<footer class="abs footer">© Ribten Lofts 2010 - All Rights Reserved</footer>

</body>
</html>
```